LANTERNHILL Pizza and Wraps

We need a website for a new restaurant called LANTERNHILL "PIZZA AND WRAPS".
I have attached fonts, background images, logo, images, content etc.
can provide you with what you need to get the website design done fast and easy
Updates

I have uploaded more images of the venue and some menu items. let me know if there is anything I need to provide to make your mission clear and easy

Reason: i would like a little time to provide more feedback to designers

Industry/Entity Type

Restaurant

Coding

Coded - Design and coding required

Number of Pages Required

5+ page

Colors

Designer to choose colors to be used in the design.

Requirements
Must have
• PAGES:
• Our Story
• Menu
• Reservations
• Catering & Delivery
• Contact

```html
<!DOCTYPE html>
<html lang="en">
<head>
<meta charset="utf-8">
<title>LANTERNHILL Pizza and Wraps</title>
<link href="https://fonts.googleapis.com/css2?family=Montserrat:wght@400;500;600;700;800&family=Orbitron:wght@400;500&family=Sacramento&display=swap" rel="stylesheet">
<style>
:root{
  --red:#ec1c24;
  --deep-red:#c8161d;
  --yellow:#fff200;
  --gold:#f6d20b;
  --black:#000;
  --ink:#1a1a1a;
  --white:#fff;
  --green:#2f9a3a;
  --grey:#777;
}
*{margin:0;padding:0;box-sizing:border-box}
html,body{width:1200px;height:2517px;overflow:hidden;background:var(--white)}
body{position:relative;font-family:"Montserrat",sans-serif;color:var(--ink)}
.abs{position:absolute}
.ph{position:absolute}
.round{border-radius:50%}

/* top bar */
.topbar{left:0;top:0;width:1200px;height:40px;background:var(--red);font-size:13px;font-weight:500;color:var(--white)}
.topbar .hours{left:637px;top:12px}
.topbar .call{left:906px;top:12px;color:var(--yellow);font-weight:600}

/* nav */
.nav{left:0;top:40px;width:1200px;height:83px;background:var(--white)}
.brand{font-family:"Montserrat",sans-serif;font-weight:800;color:var(--red);font-size:26px;letter-spacing:-.5px}
.nav .brand{left:156px;top:24px}
.menu{left:368px;top:34px;display:flex;gap:0;font-size:11.5px;font-weight:700}
.menu span{margin-right:25px}
.menu .active{color:var(--red)}
.order-btn{left:935px;top:27px;width:114px;height:30px;background:var(--yellow);color:var(--red);font-size:11.5px;font-weight:700;text-align:center;line-height:30px}

/* hero */
.hero{left:0;top:123px;width:1200px;height:468px;background:linear-gradient(100deg,#2a1d18 0%,#4a3226 45%,#6b4433 70%,#3a2820 100%)}
.hero-shade{left:0;top:123px;width:1200px;height:468px;background:rgba(0,0,0,.35)}
.hero .welcome{left:148px;top:128px;color:var(--white);font-size:22px;font-weight:600}
.hero .title{left:148px;top:160px;color:var(--white);font-size:46px;font-weight:800;line-height:50px}
.hero .title .red{color:var(--red)}
.hero .title .yel{color:var(--yellow)}
.hero .cta{left:148px;top:291px;width:161px;height:39px;border:2px solid var(--white);color:var(--white);font-size:15px;font-weight:700;text-align:center;line-height:35px}

/* intro */
.intro-shadow{left:0;top:880px;width:1200px;height:60px;background:linear-gradient(#fff,#f1f1f1 40%,#fff)}
.food{background:radial-gradient(circle,#e7a23c,#b6441f 70%,#7a2c14)}
.wrapfood{background:linear-gradient(135deg,#e9d6a8,#c79e5a 60%,#8c6a33)}
.salad{background:radial-gradient(circle,#5a8c3a,#2c3b22 70%,#151c12)}
.intro-center{left:300px;top:648px;width:600px;text-align:center}
.eyebrow{font-size:16px;font-weight:500;color:var(--red)}
.script{font-family:"Sacramento",cursive;font-size:44px;color:var(--green);line-height:44px;margin-top:4px}
.intro-center h3{font-size:13px;font-weight:700;margin-top:8px}
.intro-center p{font-size:11.5px;line-height:15px;margin-top:10px;color:#333}

/* best food */
.kicker{left:0;top:974px;width:1200px;text-align:center;font-size:11px;font-weight:700}
.best{left:0;top:1001px;width:1200px;text-align:center;font-family:"Orbitron",sans-serif;font-size:32px;color:var(--red);letter-spacing:5px}
.band{left:0;top:1347px;width:1200px;height:443px;background:linear-gradient(90deg,var(--deep-red),var(--red) 40%,#e33a3f 80%,var(--deep-red))}
.tile{position:absolute;overflow:hidden}
.tile .cap{position:absolute;left:0;width:100%;text-align:center;color:var(--white);font-weight:800}
.t-a{left:151px;top:1091px;width:420px;height:223px;background:linear-gradient(135deg,#3d5d22,#7c3b22 50%,#c9a97a)}
.t-b{left:581px;top:1091px;width:204px;height:223px;background:linear-gradient(#7a4a1c,#c98a3a 50%,#8a6a4a)}
.t-c{left:581px;top:1324px;width:204px;height:213px;background:linear-gradient(#6f6a60,#c9bfa8 60%,#8e887b)}
.t-d{left:795px;top:1091px;width:255px;height:214px;background:linear-gradient(135deg,#f0e3b2,#e2b95c 60%,#f7efd2)}
.t-e{left:151px;top:1324px;width:154px;height:213px;background:linear-gradient(135deg,#b5523c,#d8b8a8 50%,#9b4a36)}
.t-f{left:315px;top:1324px;width:256px;height:213px;background:radial-gradient(circle,#e6c56a,#d8b06a 55%,#6b4b2e)}
.t-g{left:795px;top:1314px;width:255px;height:223px;background:linear-gradient(135deg,#3a2418,#8a5a3a 55%,#2a1c14)}
.t-a .cap{top:80px;font-size:28px;line-height:30px;text-shadow:0 2px 4px rgba(0,0,0,.6)}
.t-b .cap{top:75px;font-size:22px;line-height:27px}
.t-b .sub{position:absolute;top:134px;width:100%;text-align:center;color:var(--white);font-size:10px;font-weight:700}
.t-g .cap{top:80px;font-size:17px}
.t-g .btn{position:absolute;left:27px;top:124px;width:126px;height:32px;background:var(--white);color:var(--red);font-size:12px;font-weight:700;text-align:center;line-height:32px}
.friendly{left:0;top:1618px;width:1200px;text-align:center;font-family:"Orbitron",sans-serif;font-size:34px;color:var(--gold);letter-spacing:5px}
.locate{left:0;top:1667px;width:1200px;text-align:center;font-size:12px;color:var(--white)}

/* contact strip */
.callnow{left:154px;top:1905px;font-size:21px;font-weight:700}
.callnow span{color:var(--red)}
.rule{left:154px;top:1953px;width:354px;height:2px;background:#b8a58a}
.calltext{left:154px;top:1970px;width:372px;font-size:13.5px;font-weight:600;line-height:20px;white-space:nowrap;overflow:hidden}
.phone{left:154px;top:2016px;font-size:22px;font-weight:600;color:var(--red)}
.chef{left:545px;top:1866px;width:177px;height:277px;background:linear-gradient(#f4f4f4,#e2e2e2 60%,#cfcfcf);border-radius:60px 60px 0 0}
.news{left:757px;top:1899px;font-size:21px;font-weight:700}
.news span{color:var(--red)}
.news-sub{left:757px;top:1925px;font-size:12px;font-weight:700}
.email{left:757px;top:1955px;width:287px;height:35px;border:1px solid #bbb;font-size:11px;color:#555;padding:11px 12px}
.subscribe{left:757px;top:2007px;width:144px;height:33px;background:var(--red);color:var(--white);font-size:12.5px;font-weight:700;text-align:center;line-height:33px}

/* footer */
.footer{left:0;top:2143px;width:1200px;height:374px;background:var(--black);color:var(--white)}
.footer .brand{left:151px;top:87px;font-size:30px}
.fcol{position:absolute;top:90px}
.fcol h4{font-size:14.5px;font-weight:700;margin-bottom:16px}
.fcol p{font-size:11.5px;line-height:26px}
.copy{left:151px;top:324px;font-size:9.5px}
.social{position:absolute;top:318px;width:24px;height:24px;border:2px solid var(--white);border-radius:50%}
</style>
</head>
<body>

<div class="abs topbar">
  <div class="abs hours">We Are open 10.00 AM To 11.00 PM</div>
  <div class="abs call">Call us 000-000-0000</div>
</div>

<header class="abs nav">
  <div class="abs brand">LANTERNHILL</div>
  <nav class="abs menu">
    <span class="active">HOME</span><span>OUR STORY</span><span>MENU</span><span>RESERVATIONS</span><span>CATERING &amp; DELIVERY</span><span>CONTACT</span>
  </nav>
  <div class="abs order-btn">ORDER NOW</div>
</header>

<section class="abs hero" role="img" aria-label="Restaurant storefront with brick wall and dining room seen through the windows">
  <div class="abs welcome">WELCOME TO</div>
  <div class="abs title">LANTERNHILL<br><span class="red">PIZZA</span> <span class="yel">AND WRAPS</span></div>
  <div class="abs cta">ORDER NOW</div>
</section>

<div class="abs intro-shadow"></div>
<div class="ph round food" style="left:37px;top:626px;width:75px;height:75px" role="img" aria-label="Pizza seen from above"></div>
<div class="ph round food" style="left:263px;top:628px;width:104px;height:104px" role="img" aria-label="Pizza seen from above"></div>
<div class="ph wrapfood" style="left:126px;top:730px;width:131px;height:112px;border-radius:40px" role="img" aria-label="Two stuffed wraps"></div>
<div class="ph round salad" style="left:857px;top:607px;width:146px;height:146px" role="img" aria-label="Pasta salad in a dark bowl"></div>
<div class="ph round food" style="left:988px;top:758px;width:92px;height:92px" role="img" aria-label="Pizza seen from above"></div>

<div class="abs intro-center">
  <div class="eyebrow">LET'S EAT!</div>
  <div class="script">Pizza and Wraps</div>
  <h3>WE HAVE 15 SPECIALTY PIZZAS! OR CREATE YOUR OWN!</h3>
  <p>Pizza lover's take delight in our wonderful 10" or 16" pizza. Enjoy it here, take it out, or let us deliver. Order one of our house specialty pizzas, like the Special or the Buffalo Chicken pizza. Or build your own special combination pizza from our 24 toppings.</p>
</div>

<div class="abs kicker">WE HAVE SPECIALTY PIZZAS! AND WRAPS</div>
<div class="abs best">THE BEST FOOD!</div>

<div class="abs band" role="img" aria-label="Red-tinted dining room with brick wall"></div>

<div class="tile t-a" role="img" aria-label="Stuffed pizza with greens and cheese"><div class="cap">PIZZA INSIDE<br>A PIZZA</div></div>
<div class="tile t-b" role="img" aria-label="Lamp-lit seating area"><div class="cap">LOVE AT<br>EVERY PEACE</div><div class="sub">LOREM IPSUM</div></div>
<div class="tile t-c" role="img" aria-label="Wraps with fries in a basket"></div>
<div class="tile t-d" role="img" aria-label="Grilled quesadilla slices"></div>
<div class="tile t-e" role="img" aria-label="Brick wall with restaurant sign"></div>
<div class="tile t-f" role="img" aria-label="Bowl of hummus with olive oil"></div>
<div class="tile t-g" role="img" aria-label="Warm dining room interior"><div class="cap">BEST FACILITIES</div><div class="btn">GET STARTED</div></div>

<div class="abs friendly">A FRIENDLY PIZZA &amp; GRILL</div>
<div class="abs locate">Locate yourself to start your order at LANTERNHILL Pizza &amp; Wraps</div>

<div class="abs callnow">CALL NOW FOR <span>HOME DELEVERY</span></div>
<div class="abs rule"></div>
<div class="abs calltext">Call us for more neque porro quisquam est qui do<br>ipsum quia dolor sit amet</div>
<div class="abs phone">+1 000 000 000</div>
<div class="ph wrapfood" style="left:50px;top:2047px;width:210px;height:96px;border-radius:40px" role="img" aria-label="Two stuffed wraps"></div>
<div class="ph chef" role="img" aria-label="Chef in white uniform holding a ladle and knife"></div>
<div class="abs news">OUR <span>NEWSLETTER</span></div>
<div class="abs news-sub">Receive the Latest Deals, News and More.</div>
<div class="abs email">Type your email address</div>
<div class="abs subscribe">SUBSCRIBE</div>
<div class="ph round food" style="left:1027px;top:1871px;width:60px;height:34px" role="img" aria-label="Pizza"></div>
<div class="ph round food" style="left:1057px;top:2010px;width:105px;height:55px" role="img" aria-label="Pizza"></div>
<div class="ph round food" style="left:887px;top:2058px;width:114px;height:60px" role="img" aria-label="Pizza"></div>

<footer class="abs footer">
  <div class="abs brand">LANTERNHILL</div>
  <div class="fcol" style="left:470px">
    <h4>WORKING HOURS</h4>
    <p>MON : 9.30AM TO 10.30PM<br>TUE : 9.30AM TO 10.30PM<br>WED : 9.30AM TO 10.30PM<br>THU : 9.30AM TO 10.30PM<br>FRI : 9.30AM TO 10.30PM</p>
  </div>
  <div class="fcol" style="left:713px">
    <h4>QUICK LINKS</h4>
    <p>About Us<br>Features<br>Services<br>Blog<br>Contact Us</p>
  </div>
  <div class="fcol" style="left:898px">
    <h4>CONTACT INFO</h4>
    <p>Unit 12, Block C, Ground<br>Floor, Orchard Row Plaza,<br>Lane 48-10-22,<br>RIVERBEND DISTRICT</p>
  </div>
  <div class="abs copy">© Copyrights LANTERNHILL "PIZZA AND WRAPS2017, All Rights Reserved</div>
  <div class="social" style="left:898px"></div>
  <div class="social" style="left:932px"></div>
  <div class="social" style="left:966px"></div>
  <div class="social" style="left:1000px"></div>
</footer>

</body>
</html>
```